New business card for civil engineering company - "Keystone Audit"

We need a business card designed for our new structural engineering company.

The company name is "Keystone Audit" logo files attached.

We would like the following:
* Two-sided card
* Simple design

Information to be placed on the card:
Name - Marcus Dellow
Job Title - Director / Structural Engineer
Credentials - BEng(Hons), CPEng, CMengNZ, IntPE(NZ)
Email - marcus.dellow@keystoneaudit.co.nz
mobile - 0219364058
website - www.keystoneaudit.co.nz

```html
<!DOCTYPE html>
<html lang="en">
<head>
<meta charset="utf-8">
<title>Keystone Audit — Business Card</title>
<link rel="stylesheet" href="https://fonts.googleapis.com/css2?family=Jost:wght@400;500;700&family=Open+Sans:wght@400;600;700&display=swap">
<style>
  :root {
    --navy: #134371;
    --sky: #009fe3;
    --white: #ffffff;
    --ink: #1d1d1b;
    --page: #ffffff;
  }
  * { margin: 0; padding: 0; box-sizing: border-box; }
  html, body { width: 1200px; height: 1200px; overflow: hidden; background: var(--page); }
  .canvas { position: relative; width: 1200px; height: 1200px; }

  .card { position: absolute; overflow: hidden; }

  /* Front */
  .card-front { left: 154px; top: 67px; width: 894px; height: 511px; background: var(--white); }
  .front-mark {
    position: absolute; left: 0; right: 0; top: 225px;
    display: flex; justify-content: center; align-items: center; gap: 14px;
  }
  .mark-square { width: 22px; height: 22px; background: var(--navy); }
  .front-mark .company-name {
    font-family: "Jost", sans-serif; font-weight: 500; font-size: 30px;
    letter-spacing: 3px; color: var(--ink); text-transform: uppercase;
  }
  .name-band {
    position: absolute; left: 0; top: 312px; width: 100%; height: 119px;
    background: var(--navy); display: flex; align-items: center; justify-content: center;
  }
  .name-band .company-name {
    font-family: "Jost", sans-serif; font-weight: 500; font-size: 80px;
    color: var(--white); text-transform: uppercase; letter-spacing: 1px; line-height: 1;
  }
  .web-band {
    position: absolute; left: 0; top: 445px; width: 100%; height: 40px;
    background: var(--sky); display: flex; align-items: center; justify-content: center;
    font-family: "Open Sans", sans-serif; font-size: 20px; color: var(--white); letter-spacing: 6px;
  }
  .web-band strong { font-weight: 700; }

  /* Back */
  .card-back { left: 150px; top: 622px; width: 900px; height: 513px; background: var(--white); }
  .contact-panel { position: absolute; left: 0; top: 0; width: 543px; height: 100%; background: var(--navy); color: var(--white); }
  .brand-panel {
    position: absolute; left: 553px; top: 0; width: 347px; height: 100%; background: var(--sky);
    display: flex; align-items: center; justify-content: center; gap: 12px;
  }
  .brand-panel .mark-square { background: var(--white); width: 20px; height: 20px; }
  .brand-panel .company-name {
    font-family: "Jost", sans-serif; font-weight: 500; font-size: 27px;
    letter-spacing: 2px; color: var(--white); text-transform: uppercase;
  }
  .person-name {
    position: absolute; left: 81px; top: 84px;
    font-family: "Jost", sans-serif; font-weight: 700; font-size: 42px; letter-spacing: 0.5px;
  }
  .person-role {
    position: absolute; left: 81px; top: 148px; width: 400px;
    font-family: "Open Sans", sans-serif; font-size: 20px; line-height: 29px;
  }
  .divider {
    position: absolute; left: 81px; top: 256px; width: 330px; height: 2px;
    background: linear-gradient(to right, rgba(255,255,255,0.9), rgba(255,255,255,0));
  }
  .contact-list { position: absolute; left: 80px; top: 300px; list-style: none; font-family: "Open Sans", sans-serif; font-size: 20px; }
  .contact-list li { display: flex; align-items: center; height: 42px; }
  .contact-list svg { width: 26px; height: 26px; margin-right: 18px; flex: none; }
  .contact-list .phone { font-weight: 700; font-size: 21px; }
  .contact-list strong { font-weight: 700; }
</style>
</head>
<body>
<div class="canvas">

  <section class="card card-front">
    <div class="front-mark">
      <span class="mark-square"></span>
      <span class="company-name">Keystone Audit</span>
    </div>
    <div class="name-band"><span class="company-name">Keystone Audit</span></div>
    <div class="web-band">www.<strong>keystoneaudit</strong>.co.nz</div>
  </section>

  <section class="card card-back">
    <div class="contact-panel">
      <h1 class="person-name">Marcus Dellow</h1>
      <p class="person-role">Director / Structural Engineer<br>Credentials - BEng(Hons), CPEng, CMengNZ, IntPE(NZ)</p>
      <div class="divider"></div>
      <ul class="contact-list">
        <li>
          <svg viewBox="0 0 24 24" aria-hidden="true"><path fill="#fff" d="M6.6 10.8a15.1 15.1 0 0 0 6.6 6.6l2.2-2.2c.3-.3.7-.4 1-.2 1.1.4 2.3.6 3.6.6.6 0 1 .4 1 1V20c0 .6-.4 1-1 1A17 17 0 0 1 3 4c0-.6.4-1 1-1h3.5c.6 0 1 .4 1 1 0 1.3.2 2.5.6 3.6.1.3 0 .7-.2 1z"/><path fill="none" stroke="#fff" stroke-width="1.6" d="M14 3.5a7 7 0 0 1 6.5 6.5M14 7a3.5 3.5 0 0 1 3 3"/></svg>
          <span class="phone">0219364058</span>
        </li>
        <li>
          <svg viewBox="0 0 24 24" aria-hidden="true"><circle cx="12" cy="12" r="11" fill="#fff"/><path fill="var(--navy)" d="M6.5 9.5 12 6l5.5 3.5V16h-11z"/><path fill="none" stroke="#fff" stroke-width="1.2" d="M6.5 9.5 12 13l5.5-3.5"/></svg>
          <span>marcus.dellow<strong>@keystoneaudit</strong>.co.nz</span>
        </li>
        <li>
          <svg viewBox="0 0 24 24" aria-hidden="true"><g fill="none" stroke="#fff" stroke-width="1.6"><circle cx="12" cy="12" r="10"/><ellipse cx="12" cy="12" rx="4.5" ry="10"/><path d="M2 12h20M4 6.5h16M4 17.5h16"/></g></svg>
          <span>www.<strong>keystoneaudit</strong>.co.nz</span>
        </li>
      </ul>
    </div>
    <div class="brand-panel">
      <span class="mark-square"></span>
      <span class="company-name">Keystone Audit</span>
    </div>
  </section>

</div>
</body>
</html>
```